Team email banner for internal communications

We need a team email banner/header that will be applied to all internal communications from our department to other functions. The graphic should be optimized for Outlook and be landscape in layout. We have 5 different silo within our team and will need so will either need have a blank space to denote each team or have change in colors/graphics to denote each team (see current headers attached to job description). We are looking for a banner that combines our team logo (attached) with our team name, Regional Talent & Coaching Unit. The theme should be L&D and pharmaceutical in nature.

Need extra days to review

The text in the banner should be Regional Talent & Coaching Unit with the team logo (attached).

```html
<!DOCTYPE html>
<html lang="en">
<head>
<meta charset="utf-8">
<title>Regional Talent &amp; Coaching Unit – Team Email Banners</title>
<link href="https://fonts.googleapis.com/css2?family=Montserrat:wght@500;600;700&family=Oswald:wght@600&family=Arimo&display=swap" rel="stylesheet">
<style>
  :root {
    --page: #ffffff;
    --banner-bg: #f2f8f8;
    --ink: #0b0b0b;
    --photo-dark: #c9cbcc;
    --photo-mid: #dcdedf;
    --shadow: rgba(0, 0, 0, 0.28);
    --hematology: #da2a1e;
    --solid-tumor: #cb3399;
    --leadership: #264573;
    --market-access: #04a9bc;
    --operations: #9acb36;
    --mark: #da2a1e;
  }
  * { margin: 0; padding: 0; box-sizing: border-box; }
  html, body { width: 686px; height: 1200px; overflow: hidden; background: var(--page); }
  .sheet { position: relative; width: 686px; height: 1200px; }

  .banner {
    position: absolute;
    left: 71px;
    width: 544px;
    height: 181px;
    background: var(--banner-bg);
    box-shadow: 6px 7px 6px var(--shadow);
    overflow: hidden;
  }
  .banner--hematology    { top: 96px;  --accent: var(--hematology); }
  .banner--solid-tumor   { top: 303px; --accent: var(--solid-tumor); }
  .banner--leadership    { top: 510px; --accent: var(--leadership); }
  .banner--market-access { top: 716px; --accent: var(--market-access); }
  .banner--operations    { top: 923px; --accent: var(--operations); }

  .banner__photo {
    position: absolute;
    inset: 0;
    background:
      radial-gradient(ellipse 45% 70% at 15% 45%, var(--photo-dark), transparent 70%),
      linear-gradient(100deg, var(--photo-mid) 0%, var(--photo-mid) 25%, rgba(242,248,248,0.6) 55%, rgba(242,248,248,0) 72%);
  }
  .banner__bands { position: absolute; inset: 0; width: 544px; height: 181px; }
  .banner__bands polygon { fill: var(--accent); }

  .team-mark {
    position: absolute;
    left: 64px;
    top: 58px;
    display: flex;
    align-items: center;
    gap: 5px;
  }
  .team-mark__dot { width: 10px; height: 10px; border-radius: 50%; background: var(--mark); }
  .team-mark__name {
    font-family: "Montserrat", sans-serif;
    font-weight: 700;
    font-size: 24px;
    color: var(--ink);
    letter-spacing: 0.5px;
  }

  .team-name {
    position: absolute;
    left: 155px;
    width: 322px;
    top: 46px;
  }
  .team-name__main {
    display: block;
    font-family: "Montserrat", sans-serif;
    font-weight: 600;
    font-size: 47px;
    line-height: 47px;
    color: var(--ink);
    text-align: right;
    letter-spacing: 0.5px;
  }
  .team-name__sub {
    display: flex;
    align-items: center;
    gap: 4px;
    margin-top: 5px;
    font-family: "Arimo", sans-serif;
    font-size: 13px;
    line-height: 14px;
    color: var(--ink);
    white-space: nowrap;
  }
  .team-name__rule { flex: 1; height: 1px; background: var(--ink); }

  .silo {
    position: absolute;
    right: 67px;
    top: 118px;
    font-family: "Oswald", sans-serif;
    font-weight: 600;
    font-size: 27px;
    line-height: 30px;
    color: var(--accent);
    text-align: right;
    white-space: nowrap;
    transform: scaleX(0.86);
    transform-origin: right center;
  }
</style>
</head>
<body>
<main class="sheet">

  <section class="banner banner--hematology">
    <div class="banner__photo" role="img" aria-label="Faded grey photo of medicine bottle caps with a molecular hexagon pattern"></div>
    <svg class="banner__bands" viewBox="0 0 544 181" aria-hidden="true">
      <polygon points="330,0 544,0 544,27 356,27"/>
      <polygon points="0,154 260,154 286,181 0,181"/>
    </svg>
    <div class="team-mark"><span class="team-mark__dot"></span><span class="team-mark__name">RTC</span></div>
    <h1 class="team-name">
      <span class="team-name__main">REGIONAL</span>
      <span class="team-name__sub"><span class="team-name__rule"></span>TALENT &amp; COACHING UNIT</span>
    </h1>
    <p class="silo">HEMATOLOGY</p>
  </section>

  <section class="banner banner--solid-tumor">
    <div class="banner__photo" role="img" aria-label="Faded grey photo of medicine bottle caps with a molecular hexagon pattern"></div>
    <svg class="banner__bands" viewBox="0 0 544 181" aria-hidden="true">
      <polygon points="330,0 544,0 544,27 356,27"/>
      <polygon points="0,154 260,154 286,181 0,181"/>
    </svg>
    <div class="team-mark"><span class="team-mark__dot"></span><span class="team-mark__name">RTC</span></div>
    <h2 class="team-name">
      <span class="team-name__main">REGIONAL</span>
      <span class="team-name__sub"><span class="team-name__rule"></span>TALENT &amp; COACHING UNIT</span>
    </h2>
    <p class="silo">SOLID TUMOR</p>
  </section>

  <section class="banner banner--leadership">
    <div class="banner__photo" role="img" aria-label="Faded grey photo of medicine bottle caps with a molecular hexagon pattern"></div>
    <svg class="banner__bands" viewBox="0 0 544 181" aria-hidden="true">
      <polygon points="330,0 544,0 544,27 356,27"/>
      <polygon points="0,154 260,154 286,181 0,181"/>
    </svg>
    <div class="team-mark"><span class="team-mark__dot"></span><span class="team-mark__name">RTC</span></div>
    <h2 class="team-name">
      <span class="team-name__main">REGIONAL</span>
      <span class="team-name__sub"><span class="team-name__rule"></span>TALENT &amp; COACHING UNIT</span>
    </h2>
    <p class="silo">LEADERSHIP DEVELOPMENT</p>
  </section>

  <section class="banner banner--market-access">
    <div class="banner__photo" role="img" aria-label="Faded grey photo of medicine bottle caps with a molecular hexagon pattern"></div>
    <svg class="banner__bands" viewBox="0 0 544 181" aria-hidden="true">
      <polygon points="330,0 544,0 544,27 356,27"/>
      <polygon points="0,154 260,154 286,181 0,181"/>
    </svg>
    <div class="team-mark"><span class="team-mark__dot"></span><span class="team-mark__name">RTC</span></div>
    <h2 class="team-name">
      <span class="team-name__main">REGIONAL</span>
      <span class="team-name__sub"><span class="team-name__rule"></span>TALENT &amp; COACHING UNIT</span>
    </h2>
    <p class="silo">MARKET ACCESS</p>
  </section>

  <section class="banner banner--operations">
    <div class="banner__photo" role="img" aria-label="Faded grey photo of medicine bottle caps with a molecular hexagon pattern"></div>
    <svg class="banner__bands" viewBox="0 0 544 181" aria-hidden="true">
      <polygon points="330,0 544,0 544,27 356,27"/>
      <polygon points="0,154 260,154 286,181 0,181"/>
    </svg>
    <div class="team-mark"><span class="team-mark__dot"></span><span class="team-mark__name">RTC</span></div>
    <h2 class="team-name">
      <span class="team-name__main">REGIONAL</span>
      <span class="team-name__sub"><span class="team-name__rule"></span>TALENT &amp; COACHING UNIT</span>
    </h2>
    <p class="silo">OPERATIONS &amp; CAPABILITES</p>
  </section>

</main>
</body>
</html>
```